Fine Art business needs new website

We need a simple website with a home page, about us page, New sculptures, Sold sculptures, and a contact us page.Our sculptures are very high end one of a kind pieces. As such we need the site to be VERY elegant and professional. Lastly, because I'll be updating pictures on the website on a monthly basis it needs to be user friendly to update (Wordpress is preferred). The only branding we have so far for the business is a business card.
Updates
I wasn't completely ready when this project launched, also I am on the road right now and haven't been able to be as responsive to all you designers as I would like. I will work on giving feedback to all the top designs we've received so far. Thank you all so much for your participation and hardwork.
Target Market(s)
High end customers (affluent), art collectors, interior decorators/designers
Industry/Entity Type
Art Gallery
Coding
Coded - Design and coding required
Number of Pages Required
5+ page
Requirements
Must have
- Easily editable picture gallery for myself so that I can add new pieces(pictures of the pieces), remove sold pieces, etc. I would like the website to be built in wordpress so I can update it. I currently use sitekeeperpro through Netbirch for my other business website and would like to do the same for this one.
- Pages:
- -Intro page with featured pieces
- -Current pieces gallery (for sale) mainly a picture gallery
- -Sculptures archive (sold pieces) another picture gallery
- -About us: Pull-down of -about the artist (attached content)
- -Artistic Process (attached content)
- -Show Schedule:
- -one page dedicated to "friends of QMW" (basically a link page)
- TO BE CLEAR "www.lanternhollow.com" IS A TOTALLY DIFFERENT SITE AND I'M NOT TRYING TO COMBINE THE TWO OR JOIN THEM INTO ONE. This page needs be more elegant and seperate from The Lantern Hollow site.
- UPDATE: I'd like a link to the QMW Facebook page: https://www.facebook.com/quillmarkworks/
Nice to have
- I would like the pictures on the gallery pages able to have text connected with them (Materials, price)
- I would like the site style and fonts to be similar to our business cards we've already had designed (picture attached).
Should not have
- Too much flash or other things that will make the site slow to load.

```html
<!DOCTYPE html>
<html lang="en">
<head>
<meta charset="utf-8">
<title>Quillmark Works — Fine Art Sculpted Stones</title>
<link rel="stylesheet" href="https://fonts.googleapis.com/css2?family=Libre+Baskerville:wght@400;700&family=Lato:wght@400;700&display=swap">
<style>
  :root {
    --hero-bg: #e8e8e8;
    --page-bg: #f5f5f5;
    --footer-bg: #222222;
    --ink: #333333;
    --ink-soft: #555555;
    --accent: #5b4f9a;
    --rule: #c9c9c9;
    --white: #ffffff;
    --social: #3f7fbf;
  }
  * { box-sizing: border-box; margin: 0; padding: 0; }
  html, body { width: 842px; height: 1200px; overflow: hidden; }
  body {
    position: relative;
    background: var(--page-bg);
    font-family: "Lato", sans-serif;
    color: var(--ink);
  }
  .abs { position: absolute; }

  /* Hero */
  .hero {
    position: absolute; left: 0; top: 0; width: 842px; height: 472px;
    background: var(--hero-bg);
    box-shadow: 0 2px 4px rgba(0,0,0,0.08);
  }
  .nav { position: absolute; top: 32px; left: 138px; display: flex; gap: 15px; font-size: 10px; letter-spacing: 0.2px; }
  .nav a { color: var(--ink); text-decoration: none; padding-bottom: 6px; }
  .nav a.active { border-bottom: 2px solid var(--accent); padding: 0 3px 6px; margin-left: -3px; }
  .nav .caret { display: inline-block; margin-left: 4px; vertical-align: 1px; }
  .menu-toggle { position: absolute; left: 679px; top: 32px; }
  .hero-title {
    position: absolute; top: 166px; width: 100%; text-align: center;
    font-family: "Libre Baskerville", serif; font-size: 39px; letter-spacing: 0.5px;
    color: #444; text-shadow: 0 3px 4px rgba(0,0,0,0.25);
  }
  .hero-sub {
    position: absolute; top: 219px; width: 100%; text-align: center;
    font-family: "Libre Baskerville", serif; font-size: 18px; color: #444;
    text-shadow: 0 2px 3px rgba(0,0,0,0.2);
  }
  .btn-outline {
    position: absolute; left: 375px; top: 260px; width: 93px; height: 36px;
    border: 1.5px solid var(--accent); border-radius: 2px;
    display: flex; align-items: center; justify-content: center;
    font-size: 9.5px; font-weight: 700; color: var(--accent); letter-spacing: 0.3px;
  }
  .scroll-cue { position: absolute; left: 406px; top: 394px; }

  /* Featured */
  .section-title {
    position: absolute; top: 503px; width: 100%; text-align: center;
    font-family: "Libre Baskerville", serif; font-size: 17.5px; color: var(--ink);
  }
  .section-rule { position: absolute; left: 365px; top: 537px; width: 113px; height: 1px; background: #bbb; }
  .sculpture {
    position: absolute; top: 574px; width: 150px; height: 192px;
    box-shadow: 0 3px 5px rgba(0,0,0,0.35);
  }
  .sculpture.s1 { left: 159px; background: radial-gradient(ellipse at 50% 45%, #4a3a6e 0%, #1f1a2a 40%, #161616 75%); }
  .sculpture.s2 { left: 346px; background: radial-gradient(ellipse at 50% 40%, #4c3a32 0%, #1e1a19 42%, #151515 75%); }
  .sculpture.s3 { left: 532px; background: radial-gradient(ellipse at 50% 45%, #8a5a2a 0%, #2a1e14 42%, #151515 75%); }
  .see-gallery {
    position: absolute; left: 36px; top: 126px; width: 78px; height: 30px;
    border: 1.5px solid var(--white); border-radius: 2px;
    display: flex; align-items: center; justify-content: center;
    font-size: 7.5px; font-weight: 700; color: var(--white);
  }
  .dots { position: absolute; left: 393px; top: 795px; display: flex; gap: 14px; }
  .dot { width: 8px; height: 8px; border-radius: 50%; border: 1px solid #222; }
  .dot.on { background: #222; }
  .gallery-link {
    position: absolute; top: 820px; left: 335px; font-size: 9.5px; color: var(--accent);
    display: flex; align-items: center; gap: 9px; letter-spacing: 0.2px;
  }
  .gallery-link b { font-weight: 700; }
  .divider { position: absolute; left: 150px; top: 873px; width: 542px; height: 1px; background: var(--rule); }

  /* Teasers */
  .teaser { position: absolute; top: 906px; width: 160px; }
  .teaser h3 { font-size: 13px; font-weight: 400; text-align: center; color: #222; height: 18px; }
  .teaser .t-rule { width: 82px; height: 1px; background: #bbb; margin: 5px auto 0; }
  .teaser p { margin-top: 13px; font-size: 8px; line-height: 18px; color: var(--ink-soft); width: 155px; }
  .teaser .more { margin-top: 4px; font-size: 8px; font-weight: 700; color: #222; display: flex; align-items: center; gap: 6px; }
  .t1 { left: 150px; } .t2 { left: 345px; } .t3 { left: 540px; top: 908px; }

  /* Footer */
  .footer { position: absolute; left: 0; top: 1052px; width: 842px; height: 148px; background: var(--footer-bg); color: var(--white); }
  .f-col { position: absolute; top: 28px; }
  .f-col h4 { font-size: 15px; font-weight: 700; letter-spacing: 0.1px; margin-bottom: 4px; }
  .f-col p { font-size: 8.5px; line-height: 15px; }
  .f-about { left: 138px; width: 150px; }
  .f-address { left: 369px; }
  .f-address li { list-style: none; font-size: 8.5px; line-height: 15px; display: flex; align-items: center; gap: 7px; }
  .f-address li.cta { padding-left: 17px; font-weight: 700; }
  .f-social { left: 599px; }
  .social-row { display: flex; gap: 7px; margin: 6px 0 0 20px; }
  .social-row span { width: 14px; height: 14px; background: var(--social); border-radius: 1px; }
</style>
</head>
<body>

<header class="hero">
  <nav class="nav">
    <a class="active">HOME</a>
    <a>ABOUT<svg class="caret" width="7" height="5" viewBox="0 0 7 5"><path d="M0.5 0.8 L3.5 3.8 L6.5 0.8" fill="none" stroke="#333" stroke-width="0.9"/></svg></a>
    <a>GALLERY</a>
    <a>CONTACT</a>
  </nav>
  <svg class="menu-toggle" width="25" height="14" viewBox="0 0 25 14" aria-label="Menu">
    <rect y="0" width="25" height="2" fill="#333"/><rect y="6" width="25" height="2" fill="#333"/><rect y="12" width="25" height="2" fill="#333"/>
  </svg>
  <h1 class="hero-title">QUILLMARK WORKS</h1>
  <p class="hero-sub">Fine Art Sculpted Stones</p>
  <a class="btn-outline">ABOUT US</a>
  <svg class="scroll-cue" width="30" height="78" viewBox="0 0 30 78" aria-hidden="true">
    <path d="M1 1 L15 15 L29 1 M1 8 L15 22 L29 8" fill="none" stroke="#c8c8c8" stroke-width="1.2"/>
    <path d="M1 29 L15 43 L29 29 M1 36 L15 50 L29 36" fill="none" stroke="#888" stroke-width="1.2"/>
    <path d="M1 57 L15 71 L29 57 M1 64 L15 78 L29 64" fill="none" stroke="#222" stroke-width="1.4"/>
  </svg>
</header>

<main>
  <h2 class="section-title">Featured Sculptures</h2>
  <div class="section-rule"></div>

  <div class="sculpture s1" role="img" aria-label="Amethyst geode sculpture on a stone base"></div>
  <div class="sculpture s2" role="img" aria-label="Brown mineral sculpture on a stone base">
    <span class="see-gallery">SEE GALLERY</span>
  </div>
  <div class="sculpture s3" role="img" aria-label="Polished ammonite and wood spiral sculpture"></div>

  <div class="dots"><span class="dot on"></span><span class="dot"></span><span class="dot"></span></div>
  <a class="gallery-link">
    <span>SEE MORE FROM THE <b>GALLERY</b></span>
    <svg width="17" height="9" viewBox="0 0 17 9"><path d="M0 4.5 H16 M12 1 L16 4.5 L12 8" fill="none" stroke="#5b4f9a" stroke-width="1"/></svg>
  </a>
  <div class="divider"></div>

  <article class="teaser t1">
    <h3>Meet The Artists</h3><div class="t-rule"></div>
    <p>Meet the people behind these beautiful masterpiece, their biography and the history of the Whitfield's.</p>
    <div class="more">SEE MORE <svg width="15" height="8" viewBox="0 0 15 8"><path d="M0 4 H14 M10.5 1 L14 4 L10.5 7" fill="none" stroke="#333" stroke-width="0.9"/></svg></div>
  </article>
  <article class="teaser t2">
    <h3>The Artistic Process</h3><div class="t-rule"></div>
    <p>Discover each detail of the artistic pro-cess of the creation of these fine sculp-tures from base to perfect.</p>
    <div class="more">SEE MORE <svg width="15" height="8" viewBox="0 0 15 8"><path d="M0 4 H14 M10.5 1 L14 4 L10.5 7" fill="none" stroke="#333" stroke-width="0.9"/></svg></div>
  </article>
  <article class="teaser t3">
    <h3>The Lantern Hollow</h3><div class="t-rule"></div>
    <p>Find out more about Quillmark Works's sister site, Lantern Hollow. Lorem Ipsum dolor.</p>
    <div class="more">SEE MORE <svg width="15" height="8" viewBox="0 0 15 8"><path d="M0 4 H14 M10.5 1 L14 4 L10.5 7" fill="none" stroke="#333" stroke-width="0.9"/></svg></div>
  </article>
</main>

<footer class="footer">
  <div class="f-col f-about">
    <h4>ABOUT US</h4>
    <p>This is a dummy text just<br>to provide text in the About Us<br>section which will be added correctly<br>later on.</p>
  </div>
  <div class="f-col f-address">
    <h4>OUR ADDRESS</h4>
    <ul>
      <li><svg width="10" height="10" viewBox="0 0 10 10"><path d="M2 0.5 L3.8 2.8 L2.8 4 Q4 6.3 6 7.2 L7.2 6.2 L9.5 8 L8.3 9.5 Q3.5 9 0.5 1.7 Z" fill="#fff"/></svg>(555) 214-0398</li>
      <li><svg width="10" height="8" viewBox="0 0 10 8"><rect x="0.5" y="0.5" width="9" height="7" fill="none" stroke="#fff" stroke-width="0.9"/><path d="M0.5 0.5 L5 4.5 L9.5 0.5" fill="none" stroke="#fff" stroke-width="0.9"/></svg>ellis@lanternhollow.com</li>
      <li><svg width="10" height="10" viewBox="0 0 10 10"><path d="M4 6 L6 4 M3.2 4.6 L1.6 6.2 a1.8 1.8 0 0 0 2.4 2.4 L5.6 7 M6.8 5.4 L8.4 3.8 a1.8 1.8 0 0 0 -2.4 -2.4 L4.4 3" fill="none" stroke="#fff" stroke-width="0.9"/></svg>www.quillmarkworks.com</li>
      <li class="cta">CONTACT US</li>
    </ul>
  </div>
  <div class="f-col f-social">
    <h4>KEEP IN TOUCH</h4>
    <div class="social-row" aria-label="Social links"><span></span><span></span><span></span><span></span></div>
  </div>
</footer>

</body>
</html>
```